Brambury Logistics

Create a modern, simple, Elegant business card design for my business.

Services: Tamo Trucks, Transport, Contract Logistics,

Industry/Entity Type

Business

Contact Information for Business Card

Include all details same as old card plus new website address: www.bramburylogistics.com.au

Requirements
Must have
• Similar colors to Logo.

```html
<!DOCTYPE html>
<html lang="en">
<head>
<meta charset="utf-8">
<title>Brambury Logistics – Business Card</title>
<link href="https://fonts.googleapis.com/css2?family=Roboto:wght@400;500;700&display=swap" rel="stylesheet">
<style>
  :root {
    --backdrop: #e4e4e4;
    --card: #f7f7f7;
    --ink: #2a2c2f;
    --ink-soft: #3a3d41;
    --wordmark: #4a4f56;
    --brand-blue: #1d8fcf;
    --brand-navy: #0b3b66;
    --name-blue: #1f4f86;
    --divider: #2b8fd0;
    --spine-edge: #3b3e42;
  }
  * { margin: 0; padding: 0; box-sizing: border-box; }
  html, body {
    width: 1200px; height: 576px; overflow: hidden;
    background: var(--backdrop);
    font-family: "Roboto", Arial, sans-serif;
    color: var(--ink);
  }
  .canvas { position: relative; width: 1200px; height: 576px; }
  .card {
    position: absolute;
    background: var(--card);
    border-radius: 11px;
    overflow: hidden;
  }
  /* Front */
  .card--front { left: 82px; top: 139px; width: 484px; height: 293px; }
  .wordmark {
    display: flex; align-items: center; gap: 10px;
    font-weight: 500; color: var(--wordmark);
    letter-spacing: 0.5px;
  }
  .wordmark__dot {
    width: 14px; height: 14px; border-radius: 50%;
    background: var(--brand-blue); flex: none;
  }
  .card--front .wordmark {
    position: absolute; left: 0; right: 0; top: 118px;
    justify-content: center; font-size: 30px;
  }
  .services {
    position: absolute; left: 0; right: 0; top: 387px; top: 248px;
    text-align: center; font-size: 11.5px; letter-spacing: 0.2px;
    color: var(--ink);
  }
  .services__sep { color: var(--divider); margin: 0 5px; }
  .front-band {
    position: absolute; left: 0; right: 0; bottom: 0; height: 8px;
    background: linear-gradient(90deg, var(--brand-blue), var(--brand-navy));
  }
  /* Back */
  .card--back { left: 602px; top: 138px; width: 480px; height: 291px; }
  .spine {
    position: absolute; left: 0; top: 0; bottom: 0; width: 40px;
    background: linear-gradient(180deg, var(--brand-blue), var(--brand-navy));
  }
  .spine-edge {
    position: absolute; left: 40px; top: 0; bottom: 0; width: 5px;
    background: var(--spine-edge);
  }
  .card--back .wordmark {
    position: absolute; left: 56px; top: 48px; font-size: 24px;
  }
  .person { position: absolute; left: 68px; top: 158px; }
  .person__name { font-size: 19px; font-weight: 700; color: var(--name-blue); letter-spacing: 0.6px; line-height: 1.2; }
  .person__role { font-size: 11.5px; color: var(--ink-soft); margin-top: 1px; }
  .contacts { position: absolute; left: 68px; top: 210px; list-style: none; }
  .contacts__item {
    display: flex; align-items: center; gap: 12px;
    font-size: 12.5px; color: var(--ink-soft); height: 17px;
  }
  .contacts__icon { width: 11px; height: 11px; fill: var(--name-blue); flex: none; }
</style>
</head>
<body>
<main class="canvas">
  <section class="card card--front" aria-label="Card front">
    <div class="wordmark"><span class="wordmark__dot"></span>Brambury Logistics</div>
    <p class="services">TAMO TRUCKS<span class="services__sep">|</span>TRANSPORT<span class="services__sep">|</span>CONTRACT LOGISTICS<span class="services__sep">|</span>HOTSHOTS</p>
    <div class="front-band"></div>
  </section>

  <section class="card card--back" aria-label="Card back">
    <div class="spine"></div>
    <div class="spine-edge"></div>
    <div class="wordmark"><span class="wordmark__dot"></span>Brambury Logistics</div>
    <div class="person">
      <p class="person__name">Daniel Ward</p>
      <p class="person__role">Managing Director</p>
    </div>
    <ul class="contacts">
      <li class="contacts__item">
        <svg class="contacts__icon" viewBox="0 0 12 12" aria-hidden="true"><path d="M1 3 Q1 1 3 1 L9 1 Q11 1 11 3 L11 4 L8 4 L8 3 L4 3 L4 4 L1 4 Z M2 5 L10 5 L11 11 L1 11 Z"/></svg>
        0400 563 218
      </li>
      <li class="contacts__item">
        <svg class="contacts__icon" viewBox="0 0 12 12" aria-hidden="true"><circle cx="6" cy="6" r="5.2" fill="none" stroke="#1f4f86" stroke-width="1.2"/><ellipse cx="6" cy="6" rx="2.2" ry="5.2" fill="none" stroke="#1f4f86" stroke-width="1"/><path d="M1 6 H11" stroke="#1f4f86" stroke-width="1"/></svg>
        www.bramburylogistics.com.au
      </li>
      <li class="contacts__item">
        <svg class="contacts__icon" viewBox="0 0 12 12" aria-hidden="true"><path d="M0.5 2.5 H11.5 V9.5 H0.5 Z"/><path d="M0.8 2.8 L6 6.8 L11.2 2.8" fill="none" stroke="#f7f7f7" stroke-width="1"/></svg>
        dan@bramburylogistics.com.au
      </li>
    </ul>
  </section>
</main>
</body>
</html>
```